Flyer-Design für Fitness
Sehr angaschierte Designerin, bin begeistert! Hat sofort alles umgesetzt wie wir es haben wollten. Sehr zu Empfehlen. Vielen dank an Marta
Zielgruppe
Wir haben uns zum Ziel gesetzt, unsere Kunden individuell, professionell und in einem angenehmen Ambiente 'in form' zu bringen.
Stundenlange Workouts waren gestern. Nutzen Sie heute die zeitsparenden Methoden von EMS, VIBRO DECK und KLU Training in Begleitung mit Persönlicher Betreuung, um ihre Ziele zu erreichen. Unsere Zielgruppe sind Männer und Frauen jeden Alters, die Wert auf ihr äußeres legen und sich gesund und fit halten wollen.
Homepage: www.trainingsraum-beispielort.de
Aufgabenstellung
Wir trainieren mit Vibro Deck, Swift Pulse Wear und KLU.
Der soll ein einmal Klapp Flyer sein.

```html
<!DOCTYPE html>
<html lang="de">
<head>
<meta charset="utf-8">
<title>Train to Gain – Flyer</title>
<link rel="stylesheet" href="https://fonts.googleapis.com/css2?family=Montserrat:wght@500;700;800;900&display=swap">
<style>
  :root {
    --navy: #191a33;
    --green-dark: #4a6a3c;
    --green-mid: #6e9a42;
    --green-light: #8cc63f;
    --white: #ffffff;
    --ink: #3a3a3a;
    --figure-blue: #2b3f8f;
    --figure-lime: #a6e36a;
  }
  * { margin: 0; padding: 0; box-sizing: border-box; }
  html, body { width: 849px; height: 1200px; overflow: hidden; background: var(--white); }
  .flyer {
    position: relative;
    width: 849px;
    height: 1200px;
    overflow: hidden;
    font-family: "Montserrat", Arial, sans-serif;
    background: linear-gradient(135deg, var(--green-dark) 0%, var(--green-mid) 45%, var(--green-light) 100%);
  }
  .flyer__shapes { position: absolute; inset: 0; }
  .hero-figure {
    position: absolute;
    left: 292px;
    top: 313px;
    width: 557px;
    height: 572px;
    border-radius: 48% 40% 30% 45%;
    background: radial-gradient(ellipse at 55% 40%, var(--figure-lime) 0%, #6fae4a 35%, var(--figure-blue) 75%, rgba(43,63,143,0) 100%);
    opacity: 0.85;
  }
  .headline { position: absolute; inset: 0; line-height: 1; font-size: 0; }
  .headline__train,
  .headline__gain {
    position: absolute;
    font-weight: 900;
    font-size: 150px;
    letter-spacing: -6px;
    white-space: nowrap;
  }
  .headline__train { left: 68px; top: 148px; color: var(--white); }
  .headline__gain { left: 96px; top: 302px; color: var(--navy); }
  .headline__to {
    position: absolute;
    left: 38px;
    top: 306px;
    font-weight: 800;
    font-size: 32px;
    color: var(--white);
  }
  .methods {
    position: absolute;
    left: 40px;
    top: 816px;
    display: flex;
    gap: 22px;
    list-style: none;
  }
  .method {
    width: 96px;
    display: flex;
    flex-direction: column;
    align-items: center;
    color: var(--white);
  }
  .method svg { width: 76px; height: 76px; }
  .method__label {
    margin-top: 10px;
    font-weight: 800;
    font-size: 22px;
    line-height: 1.05;
    text-align: center;
  }
  .brand {
    position: absolute;
    right: 26px;
    bottom: 28px;
    font-weight: 500;
    font-size: 38px;
    color: var(--ink);
  }
</style>
</head>
<body>
<main class="flyer">
  <svg class="flyer__shapes" viewBox="0 0 849 1200" aria-hidden="true">
    <polygon points="0,0 613,0 0,280" fill="var(--navy)"/>
  </svg>

  <div class="hero-figure" role="img" aria-label="Illustration einer sportlichen Frau im Sprung, in Blau- und Grüntönen"></div>

  <svg class="flyer__shapes" viewBox="0 0 849 1200" aria-hidden="true">
    <polygon points="849,718 849,1200 0,1200" fill="var(--white)"/>
  </svg>

  <h1 class="headline">
    <span class="headline__train">TRAIN</span>
    <span class="headline__to">TO</span>
    <span class="headline__gain">GAIN</span>
  </h1>

  <ul class="methods">
    <li class="method">
      <svg viewBox="0 0 80 80" fill="none" stroke="currentColor" stroke-width="3" stroke-linecap="round">
        <rect x="28" y="34" width="24" height="12" rx="3"/>
        <path d="M20 28 Q40 16 60 28"/>
        <path d="M12 22 Q40 4 68 22"/>
        <path d="M20 52 Q40 64 60 52"/>
        <path d="M12 58 Q40 76 68 58"/>
      </svg>
      <span class="method__label">VIBRO DECK</span>
    </li>
    <li class="method">
      <svg viewBox="0 0 80 80" fill="none" stroke="currentColor" stroke-width="3" stroke-linejoin="round" stroke-linecap="round">
        <path d="M40 70 L12 42 C2 32 6 14 22 12 C30 11 36 16 40 22 C44 16 50 11 58 12 C74 14 78 32 68 42 Z"/>
        <path d="M8 40 H28 L33 30 L39 50 L45 36 L49 40 H72"/>
      </svg>
      <span class="method__label">EMS</span>
    </li>
    <li class="method">
      <svg viewBox="0 0 80 80" fill="none" stroke="currentColor" stroke-width="3" stroke-linecap="round">
        <path d="M30 6 V30"/><path d="M50 6 V30"/>
        <path d="M26 6 H34"/><path d="M46 6 H54"/>
        <circle cx="28" cy="52" r="18"/>
        <circle cx="52" cy="52" r="18"/>
        <path d="M10 52 H70"/>
      </svg>
      <span class="method__label">KLU</span>
    </li>
  </ul>

  <p class="brand">Velotta Studio</p>
</main>
</body>
</html>
```